Design graphics and Print for a line of Herb Seeds- Envelope Design

We need a set of herb seed envelopes designed for a new seed line we are launching.
The design will be both front and back

Envelope will be a colored ( green) ) envelope with white text
or a white or cream envelope in all black /and images text. Or can add some colors to the white envelope.

I have attached the die-cut of the seed envelope.
I have attached some images of envelopes I like. Please do not copy, these are just to give you an idea of what I like.

Please feel free to reach out to me if you have any questions.

Thank you

Target Market(s)

The design needs to classic that can translate to 3 different audiences. 1. young parents 2. hip, young single millennial 3. kids

Industry/Entity Type

Ecommerce

Font styles to use
Serif

Requirements
Must have
• Please use the herb - Parsley for the design
Icon, Text or both.

Front side must have:
1.either herb Icon or work Parsley or both- this will be the main attraction
2. company name- Tin Lantern Sundries
3. can use design elements
4. can use my logo on from or back or not at all. I

Backside must have:
1. social media tags
FB, Snapshot and Pinboard ( use icons) @tinlanternsundries

my website: www.tinlanternsundries.example
this can be on from or back of the envelope.
Should not have
• please stay away from "county" flowery, old fashioned style designs

```html
<!DOCTYPE html>
<html lang="en">
<head>
<meta charset="utf-8">
<title>Tin Lantern Sundries – Parsley Seed Envelope</title>
<link rel="stylesheet" href="https://fonts.googleapis.com/css2?family=Playfair+Display:wght@700&family=Montserrat:wght@400&display=swap">
<style>
  :root {
    --envelope-green: #0b5a31;
    --ink-green: #0d3b22;
    --accent-green: #3a7a1a;
    --title-mist: #b9d3c2;
    --paper: #ffffff;
    --die-line: #2b2b2b;
    --leaf-light: #e9f2ea;
  }
  html, body { margin: 0; padding: 0; overflow: hidden; background: var(--paper); }
  .canvas { position: relative; width: 1200px; height: 1000px; background: var(--paper); overflow: hidden; }

  .panel { position: absolute; top: 168px; width: 503px; height: 697px; border: 1px solid var(--die-line); box-sizing: border-box; }
  .panel--back { left: 97px; }
  .panel--front { left: 600px; }

  .flap { position: absolute; left: 600px; top: 102px; width: 503px; height: 67px; background: var(--envelope-green); border-radius: 40px 40px 0 0; }

  .brand-block { position: absolute; left: 125px; top: 0; width: 253px; height: 304px; background: var(--envelope-green); display: flex; align-items: center; justify-content: center; }
  .brand-mark { width: 136px; height: 136px; border: 2px solid var(--paper); border-radius: 50%; display: flex; align-items: center; justify-content: center; text-align: center; color: var(--paper); font-family: "Playfair Display", serif; font-weight: 700; font-size: 17px; line-height: 1.2; }

  .back-info { position: absolute; left: 0; right: 0; top: 494px; text-align: center; color: var(--ink-green); }
  .back-info__name { font-family: "Playfair Display", serif; font-weight: 700; font-size: 31px; margin: 0; line-height: 1; }
  .back-info__tagline { font-family: "Montserrat", sans-serif; font-size: 15px; margin: 10px 0 0; color: var(--envelope-green); }
  .rule { height: 4px; background: var(--accent-green); margin: 0 auto; }
  .back-info .rule { width: 133px; margin-top: 10px; }

  .social-list { list-style: none; padding: 0; margin: 28px auto 0; width: 290px; display: grid; grid-template-columns: 150px 140px; row-gap: 4px; text-align: left; font-family: "Montserrat", sans-serif; font-size: 19px; color: var(--envelope-green); }
  .social-list li { display: flex; align-items: center; gap: 10px; }
  .social-list li::before { content: ""; width: 15px; height: 15px; border-radius: 50%; background: var(--envelope-green); flex: none; }

  .website { font-family: "Montserrat", sans-serif; font-size: 21px; color: var(--envelope-green); margin: 0; }
  .back-info .website { margin-top: 8px; }

  .front-block { position: absolute; left: 52px; top: 0; width: 397px; height: 612px; background: var(--envelope-green); text-align: center; }
  .front-block__brand { font-family: "Playfair Display", serif; font-weight: 700; font-size: 25px; color: var(--title-mist); margin: 40px 0 0; }
  .front-block__herb { font-family: "Playfair Display", serif; font-weight: 700; font-size: 47px; color: var(--paper); margin: 18px 0 0; line-height: 1; letter-spacing: 0.5px; }
  .front-block .rule { width: 156px; height: 5px; margin-top: 24px; background: #2f7a12; }
  .herb-illustration { position: absolute; left: 48px; top: 226px; width: 296px; height: 386px; border-radius: 140px 140px 0 0; background: radial-gradient(ellipse at 50% 40%, var(--leaf-light) 0%, #a9c9b2 55%, var(--envelope-green) 100%); opacity: 0.85; }

  .front-website { position: absolute; left: 0; right: 0; top: 645px; text-align: center; }
</style>
</head>
<body>
<div class="canvas">
  <div class="flap"></div>

  <section class="panel panel--back">
    <div class="brand-block">
      <div class="brand-mark">Tin Lantern<br>Sundries</div>
    </div>
    <div class="back-info">
      <h2 class="back-info__name">Tin Lantern Sundries</h2>
      <p class="back-info__tagline">Grow your Own!</p>
      <div class="rule"></div>
      <ul class="social-list">
        <li>Pinboard</li>
        <li>Snapshot</li>
        <li>Clipcast</li>
        <li>Friendbook</li>
      </ul>
      <p class="website">www.tinlanternsundries.example</p>
    </div>
  </section>

  <section class="panel panel--front">
    <div class="front-block">
      <p class="front-block__brand">Tin Lantern Sundries</p>
      <h1 class="front-block__herb">PARSLEY</h1>
      <div class="rule"></div>
      <div class="herb-illustration" role="img" aria-label="White line illustration of a flat-leaf parsley sprig with a small curly parsley sprig beside it"></div>
    </div>
    <div class="front-website"><p class="website">www.tinlanternsundries.example</p></div>
  </section>
</div>
</body>
</html>
```